Business Advisory Cards in canvas model

I need a business card to start as an individual advising in business since I am "Bachelor in Business Creation and business innovation" I would like the "Canvas Model" (basic tool to land a business) to represent a part of the logo because it is the simplest and useful model to start, I will advise on business innovation and business creation. Detail: it can be formal, dynamic, colorful, that draws attention, adapted to the millenians.

Target Market(s)

People who want to create their own company. People seeking advice on: negotiation, innovation in business, desing thingking, business creation, coaching in organizational operations, business plan and canvas model.

Contact Information for Business Card

Puede ser colorida pero formal para negociar, que se vea moderna adaptada a los millenians, que se enfoque en “el modelo canvas”.
Que ocupe toda la tarjeta de ambos lados todo el diseño.

Font styles to use
Sans Serif

Colors

Designer to choose colors to be used in the design.

Requirements
Must have
• Canvas model
Nice to have
• Make it a card that makes the person who receives it want to contact the owner of the card. Make it pleasing to the eye.
Should not have
• Negative images, colors that are lost or damage the eyesight.

```html
<!DOCTYPE html>
<html lang="es">
<head>
<meta charset="utf-8">
<title>Mateo Ramírez – Tarjeta de presentación</title>
<link rel="stylesheet" href="https://fonts.googleapis.com/css2?family=Fira+Sans:wght@500;600&display=swap">
<style>
  :root{
    --green:#0b8a3d;
    --green-tint:#17954a;
    --green-light:#3fb54f;
    --green-light-tint:#52bf60;
    --red:#c11f27;
    --red-dark:#9c161b;
    --red-panel:#d9223a;
    --orange:#d97d1f;
    --orange-tint:#e08a32;
    --ink:#111f28;
    --ink-tint:#1b2c37;
    --paper:#ffffff;
    --paper-shade:#eeeeee;
    --paper-tint:#f2f2f2;
    --grey-panel:#e6e6e6;
  }
  html,body{margin:0;padding:0;overflow:hidden;background:var(--paper);}
  .canvas{width:1200px;height:1200px;display:block;}
  .card-text{font-family:"Fira Sans",sans-serif;fill:var(--ink);}
  .card-name{font-weight:600;font-size:27px;letter-spacing:4px;}
  .card-detail{font-weight:500;font-size:14px;letter-spacing:1.4px;}
  .card-detail-lead{font-size:17px;}
  .icon-line{fill:none;stroke:#fff;stroke-width:2;stroke-linecap:round;stroke-linejoin:round;}
  .panel-line{fill:none;stroke:#fff;stroke-width:3;stroke-linecap:round;stroke-linejoin:round;}
  .chart-axis{fill:none;stroke:var(--red-panel);stroke-width:1.5;}
  .chart-bar{fill:var(--red-panel);}
  .pie-slice{fill:var(--red-dark);stroke:#fff;stroke-width:3;stroke-linejoin:round;}
</style>
</head>
<body>
<svg class="canvas" viewBox="0 0 1500 1500" xmlns="http://www.w3.org/2000/svg">
  <defs>
    <clipPath id="front-clip"><rect x="404" y="308" width="701" height="395" rx="24"/></clipPath>
    <clipPath id="back-clip"><rect x="404" y="869" width="701" height="395" rx="24"/></clipPath>
    <linearGradient id="back-paper" x1="0" y1="0" x2="0" y2="1">
      <stop offset="0" stop-color="var(--paper)"/>
      <stop offset="1" stop-color="var(--paper-shade)"/>
    </linearGradient>
  </defs>

  <!-- Front: canvas model -->
  <g class="card-front" clip-path="url(#front-clip)">
    <rect x="404" y="308" width="160" height="395" fill="var(--green)"/>
    <rect x="950" y="308" width="155" height="395" fill="var(--red-dark)"/>
    <path class="frame" fill="var(--ink)" d="M547 308 L760 300 L965 308 L965 545 L1090 660 L1090 703 L424 703 L424 660 L547 540 Z"/>
    <polygon class="block-activities" fill="var(--red-panel)" points="563,325 747,325 747,408 563,442"/>
    <polygon class="block-relations" fill="var(--orange)" points="767,325 950,325 950,442 767,408"/>
    <polygon class="block-resources" fill="var(--green-light)" points="563,458 740,425 660,585 568,540"/>
    <polygon class="block-channels" fill="var(--paper)" points="773,425 950,460 950,545 858,600"/>
    <polygon class="block-costs" fill="var(--grey-panel)" points="440,685 557,553 768,665 768,692"/>
    <polygon class="block-revenue" fill="var(--green-light)" points="788,665 965,560 1072,665 1072,685 788,692"/>

    <!-- Key partners -->
    <rect x="425" y="400" width="95" height="75" rx="6" fill="var(--green-tint)" role="img" aria-label="Sketch of a group of partners"/>

    <!-- Key activities: checklist -->
    <g class="checklist">
      <rect class="panel-line" x="599" y="340" width="16" height="16" rx="2"/>
      <rect class="panel-line" x="599" y="367" width="16" height="16" rx="2"/>
      <rect class="panel-line" x="599" y="394" width="16" height="16" rx="2"/>
      <path class="panel-line" d="M601 347 L607 355 L626 331"/>
      <path class="panel-line" d="M633 347 H694 M633 356 H680 M636 375 H686 M636 384 H676 M636 402 H696 M640 410 H690"/>
    </g>

    <!-- Customer relationships -->
    <rect x="805" y="333" width="120" height="85" rx="6" fill="var(--orange-tint)" role="img" aria-label="Sketch of three standing people"/>

    <!-- Key resources -->
    <rect x="598" y="458" width="72" height="92" rx="6" fill="var(--green-light-tint)" role="img" aria-label="Sketch of gears and a clock"/>

    <!-- Value proposition -->
    <circle cx="755" cy="540" r="46" fill="var(--ink-tint)" role="img" aria-label="Sketch of a light bulb for the value proposition"/>

    <!-- Channels -->
    <rect x="835" y="465" width="100" height="75" rx="6" fill="var(--paper-tint)" role="img" aria-label="Sketch of phone, mail, chat and laptop"/>

    <!-- Customer segments: pie chart -->
    <g class="segments-pie">
      <path class="pie-slice" d="M1030 440 L1030 402 A38 38 0 1 0 1068 440 Z"/>
      <path class="pie-slice" d="M1036 434 L1074 434 A38 38 0 0 0 1036 396 Z"/>
      <path class="pie-slice" d="M1030 440 L1003 467"/>
    </g>

    <!-- Cost structure: bar chart -->
    <g class="cost-chart">
      <path class="chart-axis" d="M543 595 V678 H645"/>
      <path class="chart-axis" d="M539 601 L543 594 L547 601 M639 674 L646 678 L639 682"/>
      <rect class="chart-bar" x="557" y="632" width="18" height="46"/>
      <rect class="chart-bar" x="582" y="617" width="18" height="61"/>
      <rect class="chart-bar" x="607" y="602" width="18" height="76"/>
    </g>

    <!-- Revenue streams -->
    <rect x="915" y="595" width="70" height="85" rx="6" fill="var(--green-light-tint)" role="img" aria-label="Sketch of a dollar sign"/>
  </g>

  <!-- Back: contact details -->
  <g class="card-back" clip-path="url(#back-clip)">
    <rect x="404" y="869" width="701" height="395" fill="url(#back-paper)"/>
    <polygon class="flag-green" fill="var(--green)" points="380,869 424,869 424,925 547,1045 547,1264 380,1264"/>
    <polygon class="flag-frame" fill="var(--ink)" points="424,869 441,869 441,918 562,1038 562,1264 547,1264 547,1045 424,925"/>
    <polygon class="flag-red" fill="var(--red)" points="1087,869 1130,869 1130,1264 965,1264 965,1045 1087,925"/>
    <polygon class="flag-frame" fill="var(--ink)" points="1070,869 1087,869 1087,925 965,1045 965,1264 948,1264 948,1038 1070,918"/>
  </g>

  <g class="contact">
    <text class="card-text card-name" x="630" y="972">MATEO RAMÍREZ</text>

    <circle cx="642" cy="1019" r="20" fill="var(--red-panel)"/>
    <path class="icon-line" d="M632 1020 L642 1011 L652 1020 M635 1018 V1029 H649 V1018 M639 1029 V1022 H645 V1029"/>
    <text class="card-text card-detail" x="673" y="1017"><tspan class="card-detail-lead">45</tspan> CALLE NORTE, MEXICO CITY,</text>
    <text class="card-text card-detail" x="673" y="1035">MEXICO</text>

    <circle cx="642" cy="1073" r="20" fill="var(--orange)"/>
    <rect class="icon-line" x="630" y="1065" width="24" height="16" rx="1"/>
    <path class="icon-line" d="M630 1066 L642 1075 L654 1066"/>
    <text class="card-text card-detail" x="673" y="1077">HOLA@MATEOASESOR.COM</text>

    <circle cx="642" cy="1128" r="20" fill="var(--green)"/>
    <path class="icon-line" d="M634 1118 L638 1117 L641 1123 L638 1126 Q641 1133 647 1136 L650 1133 L656 1136 L655 1140 Q645 1142 637 1133 Q631 1125 634 1118 Z"/>
    <text class="card-text card-detail" x="673" y="1133">+52 5550 123 4567</text>

    <circle cx="642" cy="1183" r="20" fill="var(--ink)"/>
    <circle class="icon-line" cx="642" cy="1183" r="11"/>
    <ellipse class="icon-line" cx="642" cy="1183" rx="5" ry="11"/>
    <path class="icon-line" d="M631 1183 H653"/>
    <text class="card-text card-detail" x="673" y="1191">WWW.MATEOASESOR.MX</text>
  </g>
</svg>
</body>
</html>
```